Marlowe Velvet Lashes

Business Card Needed with the winning design
information on business card needed
Tara Marlowe
0461937205
4 Bramble Street
Fernhill 3318
Eastvale
ABN: 52836190427
marlowe_velvet@mailnest.example

```html
<!DOCTYPE html>
<html lang="en">
<head>
<meta charset="utf-8">
<title>Marlowe Velvet Lashes – Business Card</title>
<link rel="stylesheet" href="https://fonts.googleapis.com/css2?family=Montserrat:wght@400;600;700&family=Kalam:wght@400&display=swap">
<style>
  :root {
    --canvas: #e9e7e4;
    --card-dark: #3a3a3c;
    --card-light: #f3f3f3;
    --band-dark: #8e8e8e;
    --band-light: #d4d4d4;
    --ink: #2b2b2b;
    --ink-soft: #555555;
    --mark-grey: #6a6a6b;
    --mark-text: #e4e4e4;
    --row-start: #f1f1f1;
    --row-end: #a9a9a9;
  }
  * { box-sizing: border-box; margin: 0; padding: 0; }
  html, body { width: 1200px; height: 723px; overflow: hidden; }
  body {
    background: var(--canvas);
    font-family: "Montserrat", sans-serif;
    position: relative;
  }
  .card {
    position: absolute;
    top: 81px;
    width: 330px;
    height: 560px;
    border-radius: 4px;
    box-shadow: 0 10px 24px rgba(0,0,0,0.18);
    overflow: hidden;
  }
  /* ---------- back (contact side) ---------- */
  .card--back {
    left: 230px;
    background: var(--card-light);
  }
  .back__band {
    position: absolute; left: 0; top: 0; bottom: 0; width: 54px;
    background: linear-gradient(90deg, var(--band-dark), var(--band-light));
  }
  .back__name-bar {
    position: absolute; left: 110px; right: 0; top: 40px; height: 44px;
    background: linear-gradient(90deg, rgba(170,170,170,0) 0%, #c4c4c4 45%, #8f8f8f 100%);
  }
  .back__name {
    position: absolute; left: 96px; top: 46px;
    font-size: 23px; font-weight: 700; color: var(--ink-soft);
    letter-spacing: -0.3px; white-space: nowrap;
  }
  .back__name span { text-transform: uppercase; color: var(--ink); }
  .contact-list {
    position: absolute; left: 54px; right: 0; top: 300px;
    list-style: none;
  }
  .contact-row {
    display: flex; align-items: center;
    min-height: 42px;
    margin-bottom: 8px;
    padding-left: 16px;
    background: linear-gradient(90deg, var(--row-start) 0%, #d8d8d8 45%, var(--row-end) 100%);
    color: var(--ink);
  }
  .contact-row--address { min-height: 64px; }
  .contact-row__icon { width: 34px; flex: 0 0 34px; display: flex; align-items: center; }
  .contact-row__label { font-size: 13px; font-weight: 600; color: #5c5c5c; }
  .contact-row__text {
    padding-left: 30px;
    font-size: 13px; font-weight: 600; letter-spacing: 1px;
    text-transform: uppercase; line-height: 1.35;
  }
  .back__email {
    position: absolute; left: 22px; bottom: 38px;
    font-family: "Kalam", cursive;
    font-size: 17px; color: var(--ink); white-space: nowrap;
  }
  /* ---------- front (brand side) ---------- */
  .card--front {
    left: 640px;
    background: var(--card-dark);
  }
  .brand {
    position: absolute; left: 0; right: 0; top: 190px;
    display: flex; flex-direction: column; align-items: center; gap: 22px;
  }
  .brand__dot {
    width: 70px; height: 70px; border-radius: 50%;
    background: var(--mark-grey);
  }
  .brand__name {
    font-family: "Montserrat", sans-serif;
    font-weight: 600; font-size: 24px; line-height: 1.3;
    color: var(--mark-text); text-align: center;
    letter-spacing: 1px;
  }
</style>
</head>
<body>
  <section class="card card--back" aria-label="Business card, contact side">
    <div class="back__band"></div>
    <div class="back__name-bar"></div>
    <h1 class="back__name">tara <span>Marlowe</span></h1>

    <ul class="contact-list">
      <li class="contact-row contact-row--address">
        <span class="contact-row__icon">
          <svg width="22" height="16" viewBox="0 0 22 16" aria-hidden="true">
            <rect x="1" y="1" width="20" height="14" fill="#7a7a7a" stroke="#5a5a5a"/>
            <polyline points="1,1 11,9 21,1" fill="none" stroke="#dcdcdc" stroke-width="1.4"/>
          </svg>
        </span>
        <span class="contact-row__text">4 Bramble Street<br>Fernhill 3318<br>Eastvale</span>
      </li>
      <li class="contact-row">
        <span class="contact-row__icon">
          <svg width="16" height="24" viewBox="0 0 16 24" aria-hidden="true">
            <rect x="1.5" y="1.5" width="13" height="21" rx="2" fill="none" stroke="#5a5a5a" stroke-width="1.6"/>
            <line x1="6" y1="19" x2="10" y2="19" stroke="#5a5a5a" stroke-width="1.4"/>
          </svg>
        </span>
        <span class="contact-row__text">0461 937 205</span>
      </li>
      <li class="contact-row">
        <span class="contact-row__icon"><span class="contact-row__label">ABN</span></span>
        <span class="contact-row__text">52836190427</span>
      </li>
    </ul>

    <p class="back__email">marlowe_velvet@mailnest.example</p>
  </section>

  <section class="card card--front" aria-label="Business card, brand side">
    <div class="brand">
      <div class="brand__dot"></div>
      <p class="brand__name">Marlowe Velvet<br>Lashes</p>
    </div>
  </section>
</body>
</html>
```